Trifold Brochure

I am looking for someone to design a marketing brochure for my construction company, We specialise in residential construction contracts which are either high end, high specification luxury homes or in volume housebuilding, i.e projects with multiple houses of apartments being built.
The format of the brochure should be A5 when folded in a trifold format
Please utilise the logo (attached), the company website (www.holvane-developments.co.uk). Please also feel free to insert any copy or images you think will be suitable.
Please also follow the guidelines below:
1. Keep it simple: Don't overload your brochure with too much text or too many images. Stick to the most important information and use bullet points or short paragraphs to make it easy for people to scan and understand.
2. Use high-quality images: Use high-resolution images that are relevant to your message and showcase your product or service in a positive light.
3. Include a call to action: Make sure your brochure includes a clear call to action, such as "Contact us today to learn more" or "Visit our website to see our full product line."
4. Use a clean, professional layout: Use a clean, uncluttered layout that is easy to read and looks professional.
5. Make it easy to read: Use a font that is easy to read and not too small.

```html
<!DOCTYPE html>
<html lang="en">
<head>
<meta charset="utf-8">
<title>Holvane Developments – Trifold Brochure</title>
<link href="https://fonts.googleapis.com/css2?family=Montserrat:wght@300;400;500;600;700;800;900&display=swap" rel="stylesheet">
<style>
:root{
  --navy:#13223d;
  --gold:#bea564;
  --gold-dark:#a98f4c;
  --grey:#5d6470;
  --white:#ffffff;
  --stage:#2a2a2a;
}
*{margin:0;padding:0;box-sizing:border-box}
html,body{width:1200px;height:2376px;overflow:hidden;background:var(--stage)}
body{position:relative;font-family:'Montserrat',sans-serif;color:var(--navy)}
.spread{position:absolute;left:40px;width:994px;height:709px;background:var(--white);transform:scale(1.1268);transform-origin:0 0;box-shadow:0 10px 30px rgba(0,0,0,.45);overflow:hidden}
.spread--outside{top:340px}
.spread--inside{top:1240px}
.abs{position:absolute}
.photo{position:absolute}
.gold{color:var(--gold)}
.navy-box{position:absolute;background:var(--navy)}
.brush{position:absolute;height:6px;border-radius:50%;background:linear-gradient(90deg,var(--gold-dark),var(--gold) 60%,rgba(190,165,100,.2))}
.body-copy{font-size:12px;line-height:14px;color:var(--grey);font-weight:400;white-space:nowrap}

/* outside spread */
.creative{left:39px;top:36px;font-size:58px;font-weight:400;color:var(--gold);letter-spacing:-.5px}
.people{left:37px;top:96px;font-size:60px;font-weight:900;letter-spacing:-1.5px}
.what{left:39px;top:222px;font-size:37px;font-weight:900;letter-spacing:-.5px}
.subhead{font-size:19px;font-weight:600;color:var(--grey)}
.numbered{font-size:14px;font-weight:800;letter-spacing:4.5px;white-space:nowrap}
.numbered .num{color:var(--gold);font-size:21px;letter-spacing:0;margin-right:18px}
.contact-title{left:347px;width:300px;top:322px;text-align:center;font-size:38px;font-weight:900;letter-spacing:-.5px}
.contact-sub{left:347px;width:300px;top:368px;text-align:center;font-size:14px;font-weight:600;color:var(--gold)}
.contact-item{position:absolute;left:0;width:304px;text-align:center;color:var(--white);font-size:13.5px;font-weight:600;line-height:17px;white-space:nowrap}
.icon-dot{position:absolute;left:140px;width:24px;height:24px;border-radius:50%;background:var(--gold);display:flex;align-items:center;justify-content:center}
.brand-name{left:674px;width:308px;top:50px;text-align:center;font-size:17px;font-weight:600;letter-spacing:2.5px;color:var(--navy)}
.interested{left:699px;top:512px;font-size:28px;font-weight:500;line-height:30px}
.working{left:697px;top:543px;font-size:41px;font-weight:900;line-height:42px;letter-spacing:-.5px}
.web{font-size:14.5px;font-weight:500;color:var(--navy);white-space:nowrap}
.web span{color:var(--gold)}

/* inside spread */
.services-title{left:39px;top:28px;font-size:39px;font-weight:900;letter-spacing:-.5px}
.svc-icon{position:absolute;left:39px;width:44px;height:44px;border:2px solid var(--navy);display:flex;align-items:center;justify-content:center}
.svc-head{position:absolute;left:99px;font-size:16px;font-weight:800}
.svc-text{position:absolute;left:99px;font-size:10.5px;line-height:12px;color:var(--grey);white-space:nowrap}
.box-heading{font-size:30px;font-weight:800;color:var(--gold);letter-spacing:.5px}
.box-text{font-size:10.5px;line-height:11.5px;color:var(--white);text-align:justify}
.why-card{position:absolute;left:345px;top:213px;width:304px;height:480px;border:2px solid var(--navy);background:var(--white)}
.why-title{position:absolute;left:0;width:100%;text-align:center}
.row{position:absolute;left:0;width:100%}
.row--gold{background:var(--gold)}
.row--gold .body-copy{color:var(--white)}
.row--gold .num{color:var(--navy)}
.brands-title{left:676px;top:208px;font-size:31px;font-weight:900;line-height:30px;letter-spacing:-.5px}
.brands-copy{left:676px;top:312px;width:290px;font-size:14px;line-height:17px;color:var(--grey)}
</style>
</head>
<body>

<!-- Outside spread -->
<section class="spread spread--outside">
  <!-- left panel -->
  <div class="abs creative">Creative</div>
  <div class="abs people">People.</div>
  <div class="brush" style="left:39px;top:183px;width:212px"></div>
  <div class="abs what">What <span class="gold">we do.</span></div>
  <div class="abs subhead" style="left:39px;top:266px">Here’s how we can help</div>
  <div class="abs numbered" style="left:39px;top:310px"><span class="num">01</span>HEADLINE 01</div>
  <p class="abs body-copy" style="left:39px;top:340px">Lorem ipsum dolor sit amet, consecte-<br>tur adipiscing elit. Nulla eget mollis<br>enim. In odio felis,</p>
  <div class="abs numbered" style="left:39px;top:400px"><span class="num">02</span>HEADLINE 01</div>
  <p class="abs body-copy" style="left:39px;top:430px">Lorem ipsum dolor sit amet, consecte-<br>tur adipiscing elit.</p>
  <div class="navy-box" style="left:0;top:480px;width:331px;height:229px"></div>
  <div class="abs" style="left:14px;top:480px;width:305px;height:209px;background:var(--white)"></div>
  <div class="photo" role="img" aria-label="Modern white villa with swimming pool" style="left:27px;top:490px;width:277px;height:187px;background:linear-gradient(180deg,#e6eef3 0%,#f4f6f6 45%,#c9c6bd 70%,#5fc8df 100%)"></div>

  <!-- middle panel -->
  <div class="photo" role="img" aria-label="White house facade with palm trees" style="left:347px;top:17px;width:300px;height:290px;background:linear-gradient(180deg,#c9d3da 0%,#dfe4e6 45%,#eef0ef 75%,#ffffff 100%)"></div>
  <div class="abs contact-title">Contact Us</div>
  <div class="abs contact-sub">Today To learn more</div>
  <div class="navy-box" style="left:345px;top:409px;width:304px;height:278px">
    <div class="icon-dot" style="top:10px"><svg width="12" height="12" viewBox="0 0 12 12"><path d="M2 2 L10 5 L6.5 6.5 L5 10 Z" fill="#fff"/></svg></div>
    <div class="contact-item" style="top:41px">www.holvane-developments.co.uk</div>
    <div class="icon-dot" style="top:76px"><svg width="12" height="12" viewBox="0 0 12 12"><path d="M3 1.5 L5 4 L4 5.3 Q5.2 7.3 6.7 8 L8 7 L10.5 9 L9 10.7 Q4.5 10.3 1.3 3 Z" fill="#fff"/></svg></div>
    <div class="contact-item" style="top:107px">020 7946 0321</div>
    <div class="icon-dot" style="top:140px"><svg width="12" height="12" viewBox="0 0 12 12"><rect x="1.5" y="3" width="9" height="6.5" fill="#fff"/><path d="M1.5 3 L6 6.8 L10.5 3" fill="none" stroke="#bea564" stroke-width="1"/></svg></div>
    <div class="contact-item" style="top:169px">info@holvane-developments.co.uk</div>
    <div class="icon-dot" style="top:199px"><svg width="12" height="12" viewBox="0 0 12 12"><path d="M6 11 Q2 6.5 2 4.5 A4 4 0 0 1 10 4.5 Q10 6.5 6 11 Z" fill="#fff"/><circle cx="6" cy="4.5" r="1.5" fill="#bea564"/></svg></div>
    <div class="contact-item" style="top:230px">Suite 12,<br>40 Marlow Lane, Redbridge, IG1 4QX</div>
  </div>

  <!-- right panel (cover) -->
  <div class="photo" role="img" aria-label="Luxury modern home with poolside terrace" style="left:674px;top:17px;width:308px;height:560px;background:linear-gradient(180deg,#eef3f5 0%,#dfeaee 20%,#b9d3d8 45%,#8fa3a0 65%,#b7d9df 82%,#ffffff 100%)"></div>
  <div class="abs brand-name">HOLVANE DEVELOPMENTS</div>
  <div class="abs interested">Interested</div>
  <div class="abs working">In Working<br>With Us?</div>
  <div class="brush" style="left:699px;top:634px;width:160px;height:5px"></div>
  <div class="abs web" style="left:699px;top:650px">www.holvane-developments<span>.co.uk</span></div>
</section>

<!-- Inside spread -->
<section class="spread spread--inside">
  <!-- left panel -->
  <div class="abs services-title">Our <span class="gold">Services</span></div>
  <div class="abs subhead" style="left:40px;top:72px">Here’s how we can help</div>

  <div class="svc-icon" style="top:122px"><svg width="26" height="20" viewBox="0 0 26 20"><path d="M2 3 L24 9 L12 11 Z M12 11 L10 17 L15 12" fill="none" stroke="#13223d" stroke-width="1.6" stroke-linejoin="round"/></svg></div>
  <div class="svc-head" style="top:120px">HEADLINE <span class="gold">01</span></div>
  <div class="svc-text" style="top:141px">Lorem ipsum dolor sit amet, eget</div>

  <div class="svc-icon" style="top:187px"><svg width="24" height="22" viewBox="0 0 24 22"><path d="M3 20 H21 M5 20 V12 H8 V20 M10.5 20 V8 H13.5 V20 M16 20 V5 H19 V20 M4 9 L11 4 L14 6 L20 2" fill="none" stroke="#13223d" stroke-width="1.5"/></svg></div>
  <div class="svc-head" style="top:185px">HEADLINE <span class="gold">02</span></div>
  <div class="svc-text" style="top:206px">dio felis, egestas ut dapibus vitae,<br>laoreet ut nisl.</div>

  <div class="svc-icon" style="top:251px"><svg width="20" height="26" viewBox="0 0 20 26"><path d="M6 18 Q6 14 3.5 11 A7 7 0 1 1 16.5 11 Q14 14 14 18 Z M7 21 H13 M8 24 H12" fill="none" stroke="#13223d" stroke-width="1.6"/></svg></div>
  <div class="svc-head" style="top:249px">HEADLINE <span class="gold">03</span></div>
  <div class="svc-text" style="top:270px">Lorem conseegestas ut dapibus<br>vitae, laor</div>

  <div class="navy-box" style="left:14px;top:327px;width:300px;height:173px">
    <div class="abs box-heading" style="left:17px;top:10px">HEADLINE</div>
    <p class="abs box-text" style="left:17px;top:55px;width:266px">Lorem ipsum dolor sit amet, consectetuer adipiscing elit, sed diam nonummy nibh euismod tincidunt. Lorem ipsum dolor sit amet.</p>
    <p class="abs box-text" style="left:17px;top:100px;width:266px">consectetuer adipiscing elit, sed diam nonummy nibh euismod tincidu Lorem ipsum dolor sit amet, consectetuer adipiscing elit, sed diam nonummy nibh euismod tincidunt. Lorem ipsum dolor sit amet.</p>
  </div>
  <div class="photo" role="img" aria-label="Contemporary timber and glass family home" style="left:14px;top:527px;width:300px;height:166px;background:linear-gradient(180deg,#f3f3f1 0%,#d8d2c6 30%,#7a5a3a 55%,#3d3a36 75%,#5a6a45 100%)"></div>

  <!-- middle & right top photo -->
  <div class="photo" role="img" aria-label="Grey shingle house with white veranda" style="left:345px;top:20px;width:637px;height:175px;background:linear-gradient(180deg,#cfd9e2 0%,#9ea3aa 35%,#e8e8e6 70%,#8c9a78 100%)"></div>

  <!-- middle panel -->
  <div class="why-card">
    <div class="why-title" style="top:8px;font-size:43px;font-weight:900;letter-spacing:-.5px">Why <span class="gold">Work</span></div>
    <div class="why-title gold" style="top:62px;font-size:29px;font-weight:800">with Us</div>
    <div class="why-title subhead" style="top:108px">The main 3 reasons</div>

    <div class="row row--gold" style="top:137px;height:78px">
      <div class="abs numbered" style="left:25px;top:10px"><span class="num">01</span>HEADLINE 01</div>
      <p class="abs body-copy" style="left:25px;top:40px">Lorem ipsum dolor sit amet, consecte-<br>tur adipiscing elit. Nulla eget mollis</p>
    </div>
    <div class="row" style="top:215px;height:98px">
      <div class="abs numbered" style="left:25px;top:20px"><span class="num">02</span>HEADLINE 02</div>
      <p class="abs body-copy" style="left:25px;top:52px">Lorem ipsum dolor sit amet, consecte-<br>tur adipiscing elit.</p>
    </div>
    <div class="row row--gold" style="top:313px;height:86px">
      <div class="abs numbered" style="left:25px;top:8px"><span class="num">03</span>HEADLINE 03</div>
      <p class="abs body-copy" style="left:25px;top:36px">Lorem ipsum dolor sit amet, consecte-<br>tur adipiscing elit. Nulla eget mollis<br>enim. In odio felis,</p>
    </div>
    <div class="row" style="top:399px;height:79px">
      <div class="abs numbered" style="left:25px;top:10px"><span class="num">04</span>HEADLINE 04</div>
      <p class="abs body-copy" style="left:25px;top:42px">Lorem ipsum dolor sit amet, consecte-<br>tur adipiscing elit.</p>
    </div>
  </div>

  <!-- right panel -->
  <div class="abs brands-title">Creativ Brands<br><span class="gold">For Creative<br>People.</span></div>
  <p class="abs brands-copy">Lorem ipsum dolor sit amet, consec-tetuer adipiscing elit, sed diam nonummy nibh .</p>
  <div class="navy-box" style="left:674px;top:387px;width:307px;height:306px">
    <div class="abs box-heading" style="left:21px;top:10px">ABOUT &nbsp;US</div>
    <p class="abs box-text" style="left:21px;top:59px;width:266px;font-size:11.5px;line-height:13px">Lorem ipsum dolor sit amet, consectetuer adipiscing elit, sed diam nonummy nibh euismod tincidunt ut.</p>
    <p class="abs box-text" style="left:21px;top:117px;width:266px;font-size:11.5px;line-height:13px">laoreet dolore magna aliquam erat volutpat. Ut wisi enim ad minim veniam, quis nostrud exerci tation ullamcorper suscipit lobortis nisl ut aliquip ex ea commodo consequat. Duis autem vel</p>
    <p class="abs box-text" style="left:21px;top:203px;width:266px;font-size:11.5px;line-height:13px">Lorem ipsum dolor sit amet, consectetuer adipiscing elit, sed diam nonummy nibh euismod tincidunt ut.laoreet dolore magna aliquam erat volutpat. Ut wisi enim ad minim veniam, quis nostrud exerci tation ullamcor-per suscipit lobortis nisl ut aliquip ex ea</p>
  </div>
</section>

</body>
</html>
```